BRASKETT LAND SERVICES BILLBOARD DESIGN

I NEED A BILLBOARD FOR MY BUSINESS. WE ARE A LAND CLEARING COMPANY AND I WOULD LIKE TO ADD A PICTURE OF MY TRACK LOADER TO THE SIGN. OPEN TO COLORS. I WOULD ALSO LIKE TO HAVE MY PHONE NUMBER 555-284-7196, WEBSITE WWW.BRASKETTLANDSERVICES.EXAMPLE, AND EMAIL ON THE SIGN (CONTACT@BRASKETTLANDSERVICES.EXAMPLE). DESIGNERS CAN HAVE THE FREEDOM TO DO WHATEVER STYLE THEY WANT AND TO USE ANY COLORS THEY WANT.

Target Market(s)

ANYONE WITH PROPERTY

Requirements
Must have
• PICTURE OF TRACK LOADER, WEBSITE, PHONE NUMBER, EMAIL
Nice to have
• OPEN TO ANYTHING
Should not have
• OPEN TO ANYTHING

```html
<!DOCTYPE html>
<html lang="en">
<head>
<meta charset="utf-8">
<title>Braskett Land Services Billboard</title>
<link href="https://fonts.googleapis.com/css2?family=Anton&family=Montserrat:wght@800&family=Oswald:wght@500&display=swap" rel="stylesheet">
<style>
  :root {
    --orange: #e2650a;
    --olive: #b8900a;
    --olive-dark: #8a6a08;
    --bar: #232a0c;
    --brown: #6a3e12;
    --white: #ffffff;
    --shadow: #2b2a0c;
    --stage: #5c5c5c;
    --photo-top: #4d6a2e;
    --photo-bottom: #a89a5a;
  }
  html, body {
    margin: 0;
    padding: 0;
    width: 1000px;
    height: 1200px;
    overflow: hidden;
    background: var(--stage);
  }
  .billboard {
    position: absolute;
    left: 40px;
    top: 370px;
    width: 920px;
    height: 460px;
    display: block;
    box-shadow: 0 18px 30px rgba(0,0,0,0.35);
  }
  .headline {
    font-family: "Anton", "Impact", sans-serif;
    font-size: 128px;
    fill: var(--white);
    filter: drop-shadow(5px 5px 0 var(--shadow));
  }
  .call-label, .phone-number {
    font-family: "Montserrat", sans-serif;
    font-weight: 800;
    fill: var(--white);
  }
  .call-label { font-size: 62px; }
  .phone-number { font-size: 68px; }
  .contact-line {
    font-family: "Oswald", sans-serif;
    font-weight: 500;
    font-size: 34px;
    fill: var(--white);
  }
  .icon-line {
    fill: none;
    stroke: var(--white);
    stroke-width: 2.5;
  }
</style>
</head>
<body>
<svg class="billboard" viewBox="0 0 1310 655" xmlns="http://www.w3.org/2000/svg">
  <defs>
    <linearGradient id="photoTone" x1="0" y1="0" x2="0" y2="1">
      <stop offset="0" stop-color="var(--photo-top)"/>
      <stop offset="0.55" stop-color="#6e7a3e"/>
      <stop offset="1" stop-color="var(--photo-bottom)"/>
    </linearGradient>
  </defs>

  <rect class="base-panel" width="1310" height="655" fill="var(--orange)"/>
  <polygon class="corner-wedge" points="0,0 115,0 0,290" fill="var(--olive)"/>

  <polygon class="accent-stripe" points="790,0 860,0 700,300 640,300" fill="var(--olive)" opacity="0.75"/>
  <polygon class="loader-photo" role="img" aria-label="Photo of an orange tracked loader with a forestry mulcher attachment on grass in front of trees"
           points="860,0 1310,0 1310,520 620,520" fill="url(#photoTone)"/>

  <polygon class="base-band-left" points="0,520 760,520 680,655 0,655" fill="var(--olive-dark)"/>
  <polygon class="base-band-right" points="1310,420 1310,655 1150,655" fill="var(--orange)"/>
  <polygon class="edge-stripe" points="1310,470 1310,655 1245,655" fill="var(--olive)"/>

  <text class="headline" x="125" y="172">BRASKETT</text>
  <text class="headline" x="125" y="294">LAND</text>
  <text class="headline" x="125" y="416">SERVICES</text>

  <polygon class="call-bar" points="85,475 1265,475 1235,560 55,560" fill="var(--bar)"/>
  <text class="call-label" x="110" y="542">CALL NOW!</text>
  <g class="phone-badge">
    <circle cx="570" cy="517" r="44" fill="var(--brown)" stroke="var(--white)" stroke-width="6"/>
    <path d="M556,494 c-6,3 -9,9 -7,17 c4,14 13,26 26,32 c6,3 13,1 16,-4 l2,-3 c1,-2 0,-4 -2,-5 l-9,-5 c-2,-1 -4,0 -5,1 l-3,4 c-7,-4 -12,-10 -15,-17 l4,-3 c2,-1 2,-3 1,-5 l-5,-10 c-1,-2 -3,-2 -5,-1 z" fill="var(--white)"/>
  </g>
  <text class="phone-number" x="628" y="543">555-284-7196</text>

  <g class="web-icon">
    <circle class="icon-line" cx="83" cy="612" r="16"/>
    <ellipse class="icon-line" cx="83" cy="612" rx="7" ry="16"/>
    <line class="icon-line" x1="67" y1="612" x2="99" y2="612"/>
    <path class="icon-line" d="M70,603 h26 M70,621 h26"/>
  </g>
  <text class="contact-line" x="112" y="626" textLength="480" lengthAdjust="spacingAndGlyphs">WWW.BRASKETTLANDSERVICES.EXAMPLE</text>

  <g class="mail-icon">
    <rect class="icon-line" x="644" y="600" width="36" height="24"/>
    <path class="icon-line" d="M644,600 l18,14 l18,-14 M644,624 l13,-12 M680,624 l-13,-12"/>
  </g>
  <text class="contact-line" x="696" y="626" textLength="548" lengthAdjust="spacingAndGlyphs">CONTACT@BRASKETTLANDSERVICES.EXAMPLE</text>
</svg>
</body>
</html>
```